Koru upkeep TV Solar Solution

Solar power system install
Services and maintenance
wiring, Rewinding and Renovation
Switch Board Upgrade
Power and lighting point
t doesn’t matter how much you spend on quality parts, your solar system will let you down if your design and installation are sub-par. Have your solar system tailored and installed by our Master Electrician and Bright Grid Guild Accredited team.

Target Market(s)

sales and installed

Industry/Entity Type

Solar install and retailer

Contact Information for Business Card

Name , Email, Phone Number ,Business address,

Font styles to use
Serif

Colors
0054AA
0677BA
7BADD7
CADEEF
E8F1F8

Requirements
Must have
• clear and bright
Nice to have
• new design
Should not have
• unclear pictures

```html
<!DOCTYPE html>
<html lang="en">
<head>
<meta charset="utf-8">
<title>Koru Upkeep – business card</title>
<link href="https://fonts.googleapis.com/css2?family=Roboto:wght@400;500;700&family=Roboto+Condensed:wght@700&display=swap" rel="stylesheet">
<style>
  :root {
    --page: #2b2b2b;
    --brand-blue: #0054AA;
    --mid-blue: #0677BA;
    --teal: #1f8f9a;
    --leaf: #6ab344;
    --sky: #7BADD7;
    --mist: #CADEEF;
    --paper: #f1f1f1;
    --band: #e4e4e4;
    --ink: #1c1c1c;
    --icon-green: #2e9a3c;
    --white: #ffffff;
  }
  * { box-sizing: border-box; margin: 0; padding: 0; }
  html, body { width: 1200px; height: 1138px; overflow: hidden; }
  body { background: var(--page); font-family: "Roboto", Arial, sans-serif; position: relative; }

  .card { position: absolute; width: 620px; height: 375px; border-radius: 16px; overflow: hidden; }

  /* front */
  .card-front {
    left: 274px; top: 186px;
    background: linear-gradient(110deg, var(--mid-blue) 0%, var(--teal) 45%, var(--leaf) 100%);
  }
  .brand-mark { position: absolute; width: 104px; height: 104px; border-radius: 50%; }
  .card-front .brand-mark { left: 118px; top: 62px; background: rgba(255,255,255,0.22); }
  .brand-name {
    position: absolute; font-family: "Roboto Condensed", "Arial Narrow", sans-serif; font-weight: 700;
    text-transform: uppercase; line-height: 1.1; letter-spacing: 1px; white-space: nowrap;
  }
  .card-front .brand-name { left: 238px; top: 106px; color: var(--white); font-size: 33px; }

  .service-band {
    position: absolute; left: 0; top: 238px; width: 100%; height: 74px;
    background: linear-gradient(180deg, #f2f2f2, var(--band));
    display: flex; flex-direction: column; justify-content: center; align-items: center; gap: 4px;
    color: var(--ink); font-size: 17px;
  }
  .service-band .sep { margin: 0 8px; }

  .web-line {
    position: absolute; left: 0; top: 331px; width: 100%;
    display: flex; justify-content: center; align-items: center; gap: 28px;
    color: var(--white); font-size: 16px;
  }
  .web-line .rule { width: 80px; height: 2px; background: rgba(255,255,255,0.6); }

  /* back */
  .card-back { left: 276px; top: 608px; background: var(--paper); }
  .person { position: absolute; left: 60px; top: 84px; color: var(--ink); }
  .person .name { color: var(--brand-blue); font-weight: 700; font-size: 25px; line-height: 32px; }
  .person .role { font-size: 16px; line-height: 22px; }
  .person .address { margin-top: 24px; font-size: 16.5px; line-height: 24px; }
  .contact-list { list-style: none; margin-top: 10px; font-size: 16.5px; }
  .contact-list li { display: flex; align-items: center; gap: 18px; height: 24px; }
  .contact-list svg { width: 14px; height: 14px; fill: var(--icon-green); }
  .contact-list .globe { fill: none; stroke: var(--icon-green); stroke-width: 1.5; }

  .card-back .brand-mark { left: 376px; top: 90px; background: var(--mist); }
  .card-back .brand-name { left: 268px; top: 222px; width: 320px; text-align: center; color: var(--brand-blue); font-size: 29px; }
</style>
</head>
<body>

<section class="card card-front">
  <div class="brand-mark" aria-hidden="true"></div>
  <div class="brand-name">Koru Upkeep<br>Energy Services</div>

  <div class="service-band">
    <p>Solar Power System Install<span class="sep">|</span>Wiring, Rewinding &amp; Renovation</p>
    <p>Services &amp; Maintenance<span class="sep">|</span>Switch Board Upgrade<span class="sep">|</span>Power &amp; Lighting Point</p>
  </div>

  <div class="web-line"><span class="rule"></span><span>www.koruupkeep.com</span><span class="rule"></span></div>
</section>

<section class="card card-back">
  <div class="person">
    <h1 class="name">John Doe Smith</h1>
    <p class="role">Managing Director</p>
    <p class="address">234 Anywhere St., Any City,<br>Any Town, US 123456</p>
    <ul class="contact-list">
      <li><svg viewBox="0 0 16 16" aria-label="phone"><path d="M1 5c0-2 3-3 7-3s7 1 7 3v1h-4V5H5v1H1zM4 7h8l2 7H2zm4 2a2 2 0 1 0 0 4 2 2 0 0 0 0-4z"/></svg>828-111-1111</li>
      <li><svg viewBox="0 0 16 16" aria-label="email"><path d="M1 3h14v10H1zm1.5 1.5L8 9l5.5-4.5v-.1H2.5zM2.5 6v5.5h11V6L8 10.5z"/></svg>john@yourwebsite.com</li>
      <li><svg viewBox="0 0 16 16" aria-label="website"><g class="globe"><circle cx="8" cy="8" r="6.5"/><ellipse cx="8" cy="8" rx="2.8" ry="6.5"/><path d="M1.5 8h13M2.6 4.8h10.8M2.6 11.2h10.8"/></g></svg>www.yourwebsite.com</li>
    </ul>
  </div>

  <div class="brand-mark" aria-hidden="true"></div>
  <div class="brand-name">Koru Upkeep<br>Energy Services</div>
</section>

</body>
</html>
```